Letterhead Design Project

I am the new owner of an existing Accouting and Financial Planning Firm (which I have been an employee at for 3 years)
We need to change the letterhead due to a change to the company's ABN etc., so thought we would like to modernise this at the same time.
We wish to keep the existing logo so there is familiarity to the clients. As per the notes on the attached document, we are happy to remove the wording from the logo, whichever will look better.
The letterhead needs to be professional, yet modern.
I will upload our logo and the required details for the letterhead.

Industry/Entity Type

Financial

Requirements
Must have
• Logo and provided business details.

```html
<!DOCTYPE html>
<html lang="en">
<head>
<meta charset="utf-8">
<title>KLR Accountants &amp; Financial Services – Letterhead</title>
<link rel="stylesheet" href="https://fonts.googleapis.com/css2?family=Open+Sans:ital,wght@0,400;1,700&family=Tinos:wght@700&display=swap">
<style>
  :root {
    --navy: #1d3f74;
    --orange: #e9a022;
    --white: #ffffff;
    --faint-navy: #e6ebf2;
  }
  * { margin: 0; padding: 0; box-sizing: border-box; }
  html, body { width: 876px; height: 1200px; overflow: hidden; background: var(--white); }
  .letterhead {
    position: relative;
    width: 876px;
    height: 1200px;
    background: var(--white);
    overflow: hidden;
  }
  .brand {
    position: absolute;
    top: 58px;
    right: 80px;
    text-align: right;
    font-family: "Tinos", "Times New Roman", serif;
    font-weight: 700;
    color: var(--navy);
  }
  .brand-mark {
    font-size: 52px;
    line-height: 1;
    letter-spacing: -1px;
  }
  .brand-name {
    margin-top: 22px;
    font-size: 16px;
    line-height: 27px;
  }
  .brand-name span { display: block; }
  .brand-accent {
    display: inline-block;
    width: 8px;
    height: 8px;
    background: var(--orange);
    margin-top: 10px;
  }
  .watermark {
    position: absolute;
    top: 545px;
    left: 0;
    width: 876px;
    text-align: center;
    font-family: "Tinos", "Times New Roman", serif;
    font-weight: 700;
    font-size: 230px;
    line-height: 0.85;
    color: var(--faint-navy);
    user-select: none;
  }
  .footer-waves {
    position: absolute;
    left: 0;
    bottom: 0;
    width: 876px;
    height: 170px;
  }
  .footer-details {
    position: absolute;
    left: 90px;
    top: 1114px;
    font-family: "Open Sans", Arial, sans-serif;
    font-size: 13.5px;
    line-height: 19px;
    color: var(--white);
  }
  .footer-details strong { font-weight: 700; font-style: italic; }
  .footer-details .sep { margin: 0 6px; }
</style>
</head>
<body>
  <main class="letterhead">
    <header class="brand">
      <div class="brand-mark">KLR</div>
      <div class="brand-name">
        <span>KLR</span>
        <span>ACCOUNTANTS</span>
        <span>&amp; FINANCIAL</span>
        <span>SERVICES</span>
      </div>
      <span class="brand-accent"></span>
    </header>

    <div class="watermark" aria-hidden="true">KLR</div>

    <svg class="footer-waves" viewBox="0 0 876 170" preserveAspectRatio="none" aria-hidden="true">
      <path fill="var(--navy)" d="M0,44 C220,18 480,48 700,88 C780,100 840,94 876,84 L876,170 L0,170 Z"/>
      <path fill="var(--orange)" d="M0,50 C240,26 490,64 710,98 C790,108 845,104 876,100 L876,122 C820,128 760,126 700,118 C480,86 240,54 0,66 Z"/>
      <path fill="var(--white)" d="M0,66 C240,54 480,86 700,118 C760,126 820,126 876,120 L876,126 C820,132 760,132 700,126 C480,94 240,64 0,74 Z"/>
      <path fill="var(--white)" d="M420,62 C540,76 640,90 720,98 C790,104 845,98 876,92 L876,98 C845,104 790,108 720,104 C640,96 540,80 420,62 Z"/>
    </svg>

    <footer class="footer-details">
      <div>ABN: 48 207 316 942</div>
      <div>12 Harcourt Street, Riverton, Vic, 3700<span class="sep">|</span>PO Box 518, Greenvale, NSW, 2650</div>
      <div><strong>Tel</strong> : 02 6000 4812<span class="sep">|</span><strong>Fax</strong> : 02 6000 4813</div>
      <div>&nbsp;<strong>Email</strong> : admin@klraccountants.com.au<span class="sep">|</span><strong>web</strong> : www.klraccountants.com.au</div>
    </footer>
  </main>
</body>
</html>
```